Restaurant Facility Equipment & Store Maintenance/

I need a flyer showing commercial/industrial kitchen equipment photos we work on Hot Equipment & Cold Equipment and offer many services. see attached highlights

```html
<!DOCTYPE html>
<html lang="en">
<head>
<meta charset="utf-8">
<title>Restaurant Facility Equipment &amp; Store Maintenance</title>
<link href="https://fonts.googleapis.com/css2?family=Poppins:wght@400;500;600;700;800&display=swap" rel="stylesheet">
<style>
  :root {
    --navy: #1f3f7d;
    --navy-deep: #1b3468;
    --red: #e1232a;
    --orange: #f26a1b;
    --sky: #35b6e9;
    --ink: #141414;
    --charcoal: #2d2d2f;
    --white: #ffffff;
    --page: #ffffff;
  }
  * { box-sizing: border-box; margin: 0; padding: 0; }
  html, body { width: 939px; height: 1200px; overflow: hidden; background: var(--page); }
  body { font-family: 'Poppins', sans-serif; color: var(--ink); }
  .flyer { position: relative; width: 939px; height: 1200px; overflow: hidden; background: var(--white); }

  .side-panel { position: absolute; left: 0; top: 0; width: 355px; height: 901px; background: var(--navy); color: var(--white); }
  .brand { position: absolute; left: 57px; top: 50px; }
  .brand-title { font-size: 42px; font-weight: 700; line-height: 1; letter-spacing: -0.5px; }
  .brand-title .warm { color: var(--orange); }
  .brand-title .cool { color: var(--sky); }
  .brand-sub { font-size: 23.5px; font-weight: 600; line-height: 1.2; margin-top: 4px; }

  .service-list { position: absolute; left: 57px; top: 173px; list-style: none; }
  .service-list li { display: flex; align-items: flex-start; height: 41px; font-size: 13.3px; line-height: 16.5px; font-weight: 500; }
  .service-list svg { width: 22px; height: 22px; margin: 2px 14px 0 0; flex: none; }

  .support-title { position: absolute; left: 57px; top: 450px; font-size: 35px; font-weight: 700; line-height: 45px; }
  .support-list { position: absolute; left: 57px; top: 558px; list-style: none; }
  .support-list li { display: flex; align-items: flex-start; font-size: 13.3px; line-height: 16.3px; font-weight: 500; margin-bottom: 8px; }
  .support-list svg { width: 16px; height: 16px; margin: 1px 12px 0 0; flex: none; }

  .certs { position: absolute; left: 0; top: 901px; width: 355px; height: 108px; background: var(--red); color: var(--white); }
  .certs h3 { position: absolute; left: 57px; top: 12px; font-size: 27px; font-weight: 700; letter-spacing: 0.3px; }
  .cert-badge { position: absolute; background: var(--white); }
  .cert-a { left: 57px; top: 62px; width: 26px; height: 26px; border-radius: 50%; }
  .cert-b { left: 190px; top: 63px; width: 26px; height: 26px; border-radius: 50%; background: #dfe6f2; }

  .headline { position: absolute; left: 397px; top: 46px; line-height: 1; }
  .headline .l1 { font-size: 38px; font-weight: 800; color: var(--ink); letter-spacing: -0.3px; }
  .headline .l2 { font-size: 70px; font-weight: 800; color: var(--navy); letter-spacing: -2px; margin-top: 2px; line-height: 66px; }
  .headline .l3 { font-size: 70px; font-weight: 800; color: var(--red); letter-spacing: -1.5px; line-height: 68px; }
  .headline .l4 { font-size: 50px; font-weight: 800; color: var(--ink); letter-spacing: -0.5px; line-height: 56px; }
  .tagline { position: absolute; left: 395px; top: 290px; font-size: 21px; font-weight: 600; color: var(--ink); }
  .location { position: absolute; left: 395px; top: 320px; font-size: 18.5px; font-weight: 500; display: flex; align-items: center; }
  .location svg { width: 16px; height: 20px; margin-right: 7px; }

  .notch { position: absolute; left: 314px; top: 345px; width: 41px; height: 38px; }
  .scope-box { position: absolute; left: 314px; top: 383px; width: 625px; height: 139px; background: var(--charcoal); color: var(--white); }
  .scope-box h4 { position: absolute; left: 50px; top: 22px; font-size: 17px; font-weight: 600; }
  .scope-item { position: absolute; display: flex; align-items: center; font-size: 16.5px; font-weight: 500; }
  .scope-item svg { width: 15px; height: 15px; margin-right: 10px; }

  .hex { position: absolute; top: 553px; width: 159px; height: 178px; }

  .why { position: absolute; left: 383px; top: 760px; }
  .why h3 { font-size: 27px; font-weight: 700; color: var(--red); letter-spacing: -0.3px; }
  .why-list { list-style: none; margin-top: 8px; }
  .why-list li { display: flex; align-items: flex-start; font-size: 13.2px; line-height: 16.3px; font-weight: 500; margin-bottom: 8px; }
  .why-list svg { width: 14px; height: 14px; margin: 1px 9px 0 0; flex: none; }

  .footer { position: absolute; left: 0; top: 1009px; width: 939px; height: 191px; background: var(--charcoal); color: var(--white); }
  .call { position: absolute; left: 57px; top: 20px; font-size: 22.5px; font-weight: 700; line-height: 24px; letter-spacing: -0.2px; }
  .slogan { position: absolute; left: 380px; top: 13px; }
  .slogan strong { display: block; font-size: 33px; font-weight: 700; color: var(--red); line-height: 36px; }
  .slogan span { display: block; font-size: 17px; font-weight: 600; line-height: 20px; margin-left: 3px; }
  .contact { position: absolute; top: 70px; display: flex; align-items: center; font-size: 14.5px; font-weight: 500; }
  .contact svg { width: 24px; height: 24px; margin-right: 13px; }
  .contact.phone { left: 57px; }
  .contact.web { left: 380px; }

  .worker { position: absolute; left: 669px; top: 743px; width: 231px; height: 457px; border-radius: 90px 90px 0 0; }
</style>
</head>
<body>
<div class="flyer">

  <aside class="side-panel">
    <div class="brand">
      <div class="brand-title"><span class="warm">Fire</span> &amp; <span class="cool">Ice</span></div>
      <div class="brand-sub">Equipment Services</div>
    </div>

    <ul class="service-list">
      <li><svg viewBox="0 0 22 22"><path d="M4 18 L15 7 M13 4 l5 5 M5 4 l13 14" stroke="#fff" stroke-width="2" fill="none" stroke-linecap="round"/><circle cx="4" cy="18" r="2" fill="#e1232a"/></svg>Installation, Repair<br>&amp; Rebuilds</li>
      <li><svg viewBox="0 0 22 22"><circle cx="11" cy="11" r="8" fill="#f5b41e"/><circle cx="11" cy="11" r="4" fill="#1f3f7d"/></svg>Preventive Maintenance<br>Programs</li>
      <li><svg viewBox="0 0 22 22"><rect x="3" y="2" width="16" height="18" rx="2" fill="#fff"/><rect x="6" y="5" width="4" height="4" fill="#e1232a"/><rect x="12" y="5" width="4" height="4" fill="#35b6e9"/><rect x="6" y="12" width="10" height="5" fill="#1f3f7d"/></svg>Equipment Cleaning &amp;<br>Refurbishing</li>
      <li><svg viewBox="0 0 22 22"><circle cx="11" cy="10" r="8" fill="#f5b41e"/><path d="M7 10 l3 3 5-6" stroke="#fff" stroke-width="2" fill="none"/></svg>OEM Parts with 30-Day<br>Warranty</li>
      <li><svg viewBox="0 0 22 22"><rect x="2" y="4" width="18" height="15" rx="1" fill="#fff"/><rect x="5" y="7" width="5" height="9" fill="#1f3f7d"/><rect x="12" y="7" width="5" height="4" fill="#1f3f7d"/></svg>Used Equipment Sales &amp;<br>Rentals</li>
      <li><svg viewBox="0 0 22 22"><circle cx="11" cy="11" r="9" fill="#fff"/><circle cx="11" cy="11" r="5" fill="none" stroke="#f26a1b" stroke-width="2.5"/></svg>CKTA-Certified<br>Technicians</li>
    </ul>

    <h2 class="support-title">Full Facility<br>Support</h2>

    <ul class="support-list">
      <li><svg viewBox="0 0 16 16"><circle cx="8" cy="8" r="8" fill="#e1232a"/><path d="M4.5 8 l2.5 2.5 4.5-5" stroke="#fff" stroke-width="1.8" fill="none"/></svg>Emergency Repairs (24/7<br>Availability)</li>
      <li><svg viewBox="0 0 16 16"><circle cx="8" cy="8" r="8" fill="#e1232a"/><path d="M4.5 8 l2.5 2.5 4.5-5" stroke="#fff" stroke-width="1.8" fill="none"/></svg>OSHA Inspections</li>
      <li><svg viewBox="0 0 16 16"><circle cx="8" cy="8" r="8" fill="#e1232a"/><path d="M4.5 8 l2.5 2.5 4.5-5" stroke="#fff" stroke-width="1.8" fill="none"/></svg>Handyman Services</li>
      <li><svg viewBox="0 0 16 16"><circle cx="8" cy="8" r="8" fill="#e1232a"/><path d="M4.5 8 l2.5 2.5 4.5-5" stroke="#fff" stroke-width="1.8" fill="none"/></svg>Electrical Upgrades<br>(Licensed Contractor)</li>
      <li><svg viewBox="0 0 16 16"><circle cx="8" cy="8" r="8" fill="#e1232a"/><path d="M4.5 8 l2.5 2.5 4.5-5" stroke="#fff" stroke-width="1.8" fill="none"/></svg>Wall, Floor &amp; Ceiling Repairs</li>
      <li><svg viewBox="0 0 16 16"><circle cx="8" cy="8" r="8" fill="#e1232a"/><path d="M4.5 8 l2.5 2.5 4.5-5" stroke="#fff" stroke-width="1.8" fill="none"/></svg>Painting, Drywall,<br>Door Closers</li>
      <li><svg viewBox="0 0 16 16"><circle cx="8" cy="8" r="8" fill="#e1232a"/><path d="M4.5 8 l2.5 2.5 4.5-5" stroke="#fff" stroke-width="1.8" fill="none"/></svg>Restaurant Furniture<br>Repair/Replacement</li>
      <li><svg viewBox="0 0 16 16"><circle cx="8" cy="8" r="8" fill="#e1232a"/><path d="M4.5 8 l2.5 2.5 4.5-5" stroke="#fff" stroke-width="1.8" fill="none"/></svg>Décor, Signage, Parking Lot<br>&amp; Dumpster Area Repairs</li>
      <li><svg viewBox="0 0 16 16"><circle cx="8" cy="8" r="8" fill="#e1232a"/><path d="M4.5 8 l2.5 2.5 4.5-5" stroke="#fff" stroke-width="1.8" fill="none"/></svg>Food Service Truck<br>Equipment Repairs</li>
    </ul>
  </aside>

  <section class="certs">
    <h3>CERTIFICATIONS</h3>
    <div class="cert-badge cert-a" role="img" aria-label="Certification badge"></div>
    <div class="cert-badge cert-b" role="img" aria-label="Certification badge"></div>
  </section>

  <header class="headline">
    <div class="l1">RESTAURANT FACILITY</div>
    <div class="l2">EQUIPMENT</div>
    <div class="l3">&amp; STORE</div>
    <div class="l4">MAINTENANCE</div>
  </header>
  <p class="tagline">Commercial &amp; Industrial Kitchen Services</p>
  <p class="location"><svg viewBox="0 0 16 20"><path d="M8 0 C3.6 0 0 3.4 0 7.6 C0 13 8 20 8 20 S16 13 16 7.6 C16 3.4 12.4 0 8 0Z" fill="#e1232a"/><circle cx="8" cy="7.5" r="3" fill="#fff"/></svg>Denver Metro &amp; Surrounding Areas</p>

  <svg class="notch" viewBox="0 0 41 38"><polygon points="41,0 41,38 0,38" fill="#141414"/></svg>
  <section class="scope-box">
    <h4>We Handle Everything From the Front Door to the Back Door</h4>
    <div class="scope-item" style="left:50px;top:54px"><svg viewBox="0 0 16 16"><circle cx="8" cy="8" r="8" fill="#fff"/><path d="M4.5 8 l2.5 2.5 4.5-5" stroke="#2d2d2f" stroke-width="1.8" fill="none"/></svg>Installation</div>
    <div class="scope-item" style="left:264px;top:54px"><svg viewBox="0 0 16 16"><circle cx="8" cy="8" r="8" fill="#fff"/><path d="M4.5 8 l2.5 2.5 4.5-5" stroke="#2d2d2f" stroke-width="1.8" fill="none"/></svg>OSHA Inspection</div>
    <div class="scope-item" style="left:50px;top:88px"><svg viewBox="0 0 16 16"><circle cx="8" cy="8" r="8" fill="#fff"/><path d="M4.5 8 l2.5 2.5 4.5-5" stroke="#2d2d2f" stroke-width="1.8" fill="none"/></svg>Rebuilds</div>
    <div class="scope-item" style="left:264px;top:88px"><svg viewBox="0 0 16 16"><circle cx="8" cy="8" r="8" fill="#fff"/><path d="M4.5 8 l2.5 2.5 4.5-5" stroke="#2d2d2f" stroke-width="1.8" fill="none"/></svg>Preventive Maintenance Services</div>
  </section>

  <svg class="hex" style="left:369px" viewBox="0 0 159 178" role="img" aria-label="Photo of a commercial kitchen with pots and shelving">
    <defs><linearGradient id="hexA" x1="0" y1="0" x2="0" y2="1"><stop offset="0" stop-color="#3a4150"/><stop offset="1" stop-color="#9aa3ad"/></linearGradient></defs>
    <polygon points="79.5,3 156,46 156,132 79.5,175 3,132 3,46" fill="url(#hexA)" stroke="#1f3f7d" stroke-width="5"/>
  </svg>
  <svg class="hex" style="left:551px" viewBox="0 0 159 178" role="img" aria-label="Photo of stainless steel beverage urns">
    <defs><linearGradient id="hexB" x1="0" y1="0" x2="0" y2="1"><stop offset="0" stop-color="#b8b4a8"/><stop offset="0.7" stop-color="#6e6a60"/><stop offset="1" stop-color="#2a2620"/></linearGradient></defs>
    <polygon points="79.5,3 156,46 156,132 79.5,175 3,132 3,46" fill="url(#hexB)" stroke="#1f3f7d" stroke-width="5"/>
  </svg>
  <svg class="hex" style="left:727px" viewBox="0 0 159 178" role="img" aria-label="Photo of a stainless steel kitchen fryer line">
    <defs><linearGradient id="hexC" x1="0" y1="0" x2="0" y2="1"><stop offset="0" stop-color="#c9c6bd"/><stop offset="1" stop-color="#7f7e78"/></linearGradient></defs>
    <polygon points="79.5,3 156,46 156,132 79.5,175 3,132 3,46" fill="url(#hexC)" stroke="#1f3f7d" stroke-width="5"/>
  </svg>

  <section class="why">
    <h3>Why Choose Us?</h3>
    <ul class="why-list">
      <li><svg viewBox="0 0 16 16"><circle cx="8" cy="8" r="8" fill="#1f3f7d"/><path d="M4.5 8 l2.5 2.5 4.5-5" stroke="#fff" stroke-width="1.8" fill="none"/></svg>CKTA Certified Technicians</li>
      <li><svg viewBox="0 0 16 16"><circle cx="8" cy="8" r="8" fill="#1f3f7d"/><path d="M4.5 8 l2.5 2.5 4.5-5" stroke="#fff" stroke-width="1.8" fill="none"/></svg>OEM Parts for Maximum Reliability</li>
      <li><svg viewBox="0 0 16 16"><circle cx="8" cy="8" r="8" fill="#1f3f7d"/><path d="M4.5 8 l2.5 2.5 4.5-5" stroke="#fff" stroke-width="1.8" fill="none"/></svg>Preventive Maintenance Subscribers<br>Save on Labor Rates</li>
      <li><svg viewBox="0 0 16 16"><circle cx="8" cy="8" r="8" fill="#1f3f7d"/><path d="M4.5 8 l2.5 2.5 4.5-5" stroke="#fff" stroke-width="1.8" fill="none"/></svg>Rapid Dispatch of Skilled Technicians</li>
      <li><svg viewBox="0 0 16 16"><circle cx="8" cy="8" r="8" fill="#1f3f7d"/><path d="M4.5 8 l2.5 2.5 4.5-5" stroke="#fff" stroke-width="1.8" fill="none"/></svg>Local &amp; Trusted in the Denver<br>Metro Area</li>
      <li><svg viewBox="0 0 16 16"><circle cx="8" cy="8" r="8" fill="#1f3f7d"/><path d="M4.5 8 l2.5 2.5 4.5-5" stroke="#fff" stroke-width="1.8" fill="none"/></svg>Graffiti Removal Services Available</li>
    </ul>
  </section>

  <footer class="footer">
    <p class="call">CALL TODAY FOR FAST,<br>PROFESSIONAL SERVICE</p>
    <div class="slogan"><strong>We fix it all</strong><span>if you have it, we probably fix it.</span></div>
    <p class="contact phone"><svg viewBox="0 0 24 24"><circle cx="12" cy="12" r="12" fill="#e1232a"/><path d="M8 6 l2.5 0 1 3 -1.5 1.2 c0.8 1.6 2 2.8 3.6 3.6 l1.2-1.5 3 1 0 2.5 c-6 0.5 -10.3-3.8 -9.8-9.8z" fill="#fff"/></svg>555 -014-2876</p>
    <p class="contact web"><svg viewBox="0 0 24 24"><circle cx="12" cy="12" r="12" fill="#e1232a"/><g stroke="#fff" stroke-width="1.3" fill="none"><circle cx="12" cy="12" r="6.5"/><ellipse cx="12" cy="12" rx="3" ry="6.5"/><path d="M5.5 12h13M6.5 8.8h11M6.5 15.2h11"/></g></svg>www.fireicefacility.com</p>
  </footer>

  <div class="worker" role="img" aria-label="Photo of a smiling technician in blue coveralls and cap with a tool belt, arms crossed" style="background:linear-gradient(180deg,#2b4fb0 0%,#2347a3 60%,#c9a46a 78%,#2347a3 90%)"></div>

</div>
</body>
</html>
```